IT Consulting Site Revamping for Marlune

I've put a skeleton together on my website, but realize I need some help (it's http://pilot.marlune-example.ca).
I've pulled together tidbits from other websites, but really need my site to be cleaned up, and really spruced up.
I primarily focus on the IT needs of small to medium size businesses, taking care of everything from their servers and networks down to their workstations.
I also want a page listing the vendors (and logos) that I work with including Quillsoft, Zentrix, Halvor, Brax, TL, RZO, VELK, Trevo, Gatemoor.
There should also be a simple form to get a quote that will email me.
The final design should communicate strength and reliability.
I would like this to be a fully functional website, that I can upload to Plumly Pages, with the same sort of pages that are existing on http://pilot.marlune-example.ca
Updates
Hey everyone,
Hi everyone,
Reason: Hi all,
There are some designers that would like to submit some new designs, so I'm extending the deadline.
Thanks,
Target Market(s)
Small to medium size business owners. This will primarily be males who work in the oil and gas industry.
Industry/Entity Type
Consulting
Look and feel
Each slider illustrates characteristics of the customer's brand and the style your logo design should communicate.

```html
<!DOCTYPE html>
<html lang="en">
<head>
<meta charset="utf-8">
<title>Marlune Solutions</title>
<link rel="stylesheet" href="https://fonts.googleapis.com/css2?family=Oswald:wght@300;400&family=Signika:wght@400&family=Arimo:ital,wght@0,400;1,400&display=swap">
<style>
:root{
  --navy:#2b5080;
  --deep:#023768;
  --nav-top:#1f3f6e;
  --nav-bot:#0c2a55;
  --heading-blue:#1d4f91;
  --sky:#4da3e8;
  --link:#3f83c9;
  --grey-text:#6e6e6e;
  --band:#c9c9c9;
  --page:#efefef;
  --orange:#e0661c;
  --managed:#4f8fd0;
  --storage:#2d5587;
  --network:#0f2446;
  --white:#ffffff;
}
*{margin:0;padding:0;box-sizing:border-box}
html,body{width:1029px;height:1200px;overflow:hidden}
body{position:relative;background:var(--page);font-family:Arimo,Arial,sans-serif;color:var(--grey-text)}
.abs{position:absolute}
a{text-decoration:none}
.top-band{left:0;top:0;width:1029px;height:429px;background:var(--navy)}

.brand{left:142px;top:20px;display:flex;align-items:center;gap:16px}
.brand-mark{width:78px;height:78px;border-radius:50%;background:var(--white)}
.brand-name{font-family:Oswald,sans-serif;font-weight:400;font-size:50px;color:var(--white);letter-spacing:1px}

.site{left:88px;top:116px;width:860px;height:1063px}
.nav{left:0;top:0;width:860px;height:53px;border-radius:12px 12px 0 0;
  background:linear-gradient(var(--nav-top),var(--nav-bot));display:flex;justify-content:center;align-items:center;border:1px solid #3b5f92;border-bottom:0}
.nav a{font-family:Signika,sans-serif;font-size:17px;color:var(--white);padding:0 23px;border-right:1px solid #c9d4e4;line-height:26px}
.nav a:last-child{border-right:0}

.hero{left:0;top:53px;width:860px;height:276px;background:#e9e9e9}
.hero-photo{left:460px;top:0;width:400px;height:276px;
  background:linear-gradient(90deg,rgba(233,233,233,1) 0%,#9aa3ae 18%,#4f5a68 55%,#8a96a6 100%)}
.hero-deco{left:0;top:0;width:460px;height:276px;background:radial-gradient(circle at 42% 55%,#c9d6e6 0%,#dfe4ea 45%,#e9e9e9 75%)}
.hero-kicker{left:53px;top:66px;font-family:Oswald,sans-serif;font-weight:300;font-size:34px;color:#4a4a4a;letter-spacing:-.3px}
.hero-title{left:53px;top:108px;font-family:Oswald,sans-serif;font-weight:400;font-size:46px;line-height:52px;color:var(--heading-blue);letter-spacing:-.5px}

.services{left:0;top:329px;width:860px;height:145px;background:var(--band);border-top:1px solid #b8b8b8}
.services .dot{position:absolute;top:7px;width:16px;height:16px;border-radius:50%}
.services h3{position:absolute;top:27px;font-family:Oswald,sans-serif;font-weight:300;font-size:17px;line-height:22px;letter-spacing:-.2px;white-space:nowrap}
.services p{position:absolute;top:60px;width:140px;font-size:10.3px;line-height:12.4px;color:var(--grey-text)}
.services .more{position:absolute;top:123px;font-size:10.3px;font-style:italic}

.middle{left:0;top:474px;width:860px;height:286px;background:linear-gradient(#e6e6e6,#f2f2f2)}
.section-title{font-family:Oswald,sans-serif;font-weight:300;font-size:19px}
.products{left:35px;top:33px;width:480px}
.product{position:absolute;left:0;width:480px;font-size:10.3px;line-height:12.4px}
.product h4{font-weight:400;font-size:10.3px;color:var(--sky)}
.product p{width:470px}
.product .more{position:absolute;left:371px;color:var(--link);white-space:nowrap}
.testimonials{left:576px;top:33px;width:258px}
.quote{position:absolute;left:0;width:258px;font-size:10.3px;line-height:12.4px}
.quote svg{position:absolute;left:0;top:0}
.quote p{text-indent:26px}
.quote cite{display:block;color:var(--link);font-style:italic}

.about{left:0;top:760px;width:860px;height:149px;background:var(--navy)}
.about h2{position:absolute;left:37px;top:20px;font-family:Oswald,sans-serif;font-weight:400;font-size:19px;color:var(--white)}
.about p{position:absolute;left:37px;width:790px;font-size:10.3px;line-height:12.2px;color:var(--white)}

.footer{left:0;top:909px;width:860px;height:154px;background:var(--deep);border-radius:0 0 12px 12px}
.footer-links{position:absolute;left:41px;top:40px;display:flex}
.footer-links a{font-size:10.5px;color:var(--white);margin-right:30px}
.footer-brand{position:absolute;left:468px;top:64px;display:flex;align-items:center;gap:8px}
.footer-brand span:first-child{width:30px;height:30px;border-radius:50%;background:var(--white)}
.footer-brand span:last-child{font-family:Oswald,sans-serif;font-size:20px;color:var(--white)}
.copy{position:absolute;left:44px;top:115px;font-size:10.5px;font-style:italic;color:var(--white)}
.contact h2{position:absolute;left:646px;top:16px;font-family:Oswald,sans-serif;font-weight:400;font-size:19px;color:var(--white)}
.contact p{position:absolute;left:648px;font-size:10.5px;line-height:15.5px;color:var(--white)}
</style>
</head>
<body>
<div class="abs top-band"></div>

<div class="abs brand">
  <span class="brand-mark"></span>
  <span class="brand-name">Marlune</span>
</div>

<div class="abs site">
  <nav class="abs nav">
    <a href="#">HOME</a><a href="#">OUR SERVICES</a><a href="#">ABOUT US</a><a href="#">OUR PRODUCTS</a><a href="#">CONTACT US</a>
  </nav>

  <section class="abs hero">
    <div class="abs hero-deco" role="img" aria-label="Faint large flower shape on a dotted light grey background"></div>
    <div class="abs hero-photo" role="img" aria-label="Photo of an IT technician standing with arms crossed in a server room"></div>
    <div class="abs hero-kicker">BUSINESS INFORMATION SOLUTIONS</div>
    <div class="abs hero-title">EASY, AFFORDABLE<br>AND RELIABLE.</div>
  </section>

  <section class="abs services">
    <span class="dot" style="left:95px;background:var(--managed)"></span>
    <h3 style="left:29px;color:var(--managed)">MANAGED IT SERVICES</h3>
    <p style="left:31px">Marlune is an IT outsourcing provider supplying small and medium sized businesses like yours with networking solutions, desktop services,</p>
    <a class="more" style="left:101px;color:var(--managed)">read more &gt;</a>

    <span class="dot" style="left:303px;background:var(--storage)"></span>
    <h3 style="left:225px;color:var(--storage)">STORAGE AND VIRTUALIZATION</h3>
    <p style="left:250px">Marlune's Storage and Virtualization Services incorporate ongoing support, maintenance, operations and management of the ICT</p>
    <a class="more" style="left:329px;color:var(--storage)">read more &gt;</a>

    <span class="dot" style="left:533px;background:var(--network)"></span>
    <h3 style="left:495px;color:var(--network)">NETWORKING</h3>
    <p style="left:476px">Marlune can help your small business keep your computer network under control. We are a complete network solution provider that focuses</p>
    <a class="more" style="left:553px;color:var(--network)">read more &gt;</a>

    <span class="dot" style="left:730px;background:var(--orange)"></span>
    <h3 style="left:666px;color:var(--orange)">BACKUP AND RECOVERY</h3>
    <p style="left:674px">Your small business data is growing and data loss happens for many reasons. Hard drive crashes, viruses, hardware failure, fires,</p>
    <a class="more" style="left:745px;color:var(--orange)">read more &gt;</a>
  </section>

  <section class="abs middle">
    <div class="abs products">
      <h2 class="section-title" style="color:var(--sky)">OUR PRODUCTS</h2>
      <div class="product" style="top:39px">
        <h4>Computer Networking</h4>
        <p>Marlune can help your small business keep your computer network under control. We are a complete network solution provider that focuses on resource sharing, remote access, system security and software application sharing for small businesses...</p>
        <a class="more" style="top:37px">more details &gt;</a>
      </div>
      <div class="product" style="top:101px">
        <h4>Firewalls</h4>
        <p>Marlune can help your business limit employees internet access to social network sites such as...</p>
        <a class="more" style="top:25px">more details &gt;</a>
      </div>
      <div class="product" style="top:138px">
        <h4>VPN's (Virtual Private Networks)</h4>
        <p>Marlune can help your small business implement, maintain and configure your virtual private network (VPN) to provide remote offices or individual users with secure access to...</p>
        <a class="more" style="top:25px">more details &gt;</a>
      </div>
      <div class="product" style="top:186px">
        <h4>Remote Access</h4>
        <p style="width:400px">Remote access allows you to work from home or anywhere in the world. Marlune can help you create a remote office that you can access from the road. We can...</p>
        <a class="more" style="top:25px">more details &gt;</a>
      </div>
    </div>

    <div class="abs testimonials">
      <h2 class="section-title" style="color:#333;text-align:center">TESTIMONIALS</h2>
      <div class="quote" style="top:35px">
        <svg width="20" height="20" viewBox="0 0 20 20"><path d="M1 1h5l7 9-7 9H1l7-9zM8 1h5l7 9-7 9H8l7-9z" fill="#1d4f91"/></svg>
        <p style="padding-top:10px">Proin gravida nibh vel velit auctor aliquet. Aenean sollicitudin, lorem quis bibendum auctor, nisi elit consequat ipsum, nec sagittis sem nibh id elit. Duis sed odio sit amet nibh vulputate cursus a sit amet mauris. Morbi accumsan ipsum velit. Nam nec tellus a odio tincidunt auctor a ornare odio.</p>
        <cite>Aenean sollicitudin, lorem quis bibendum auctor</cite>
      </div>
      <div class="quote" style="top:146px">
        <svg width="20" height="20" viewBox="0 0 20 20"><path d="M1 1h5l7 9-7 9H1l7-9zM8 1h5l7 9-7 9H8l7-9z" fill="#1d4f91"/></svg>
        <p style="padding-top:10px">Sed non mauris vitae erat consequat auctor eu in elit. Class aptent taciti sociosqu ad litora torquent per conubia nostra, per inceptos himenaeos. Mauris in erat justo. Nullam ac urna eu felis dapibus condimentum sit amet a augue. Sed non neque elit. Sed ut imperdiet nisi. Proin condimentum fermentum nunc.</p>
        <cite>Aenean sollicitudin, lorem quis bibendum auctor</cite>
      </div>
    </div>
  </section>

  <section class="abs about">
    <h2>SHORTLY ABOUT US</h2>
    <p style="top:54px">Marlune Solutions is a computer solutions provider and IT consulting firm that supports a wide variety of local small businesses in the Calgary area primarily. Our company also provides IT services to businesses throughout Alberta on special projects.</p>
    <p style="top:91px">Marlune has been trusted for over the last 7 years by small business companies like yours. Whether you are looking for an ongoing computer support company, looking to outsource your small business computer work, or just looking for a computer company to help you solve a computer problem, Marlune is your right choice.</p>
  </section>

  <footer class="abs footer">
    <div class="footer-links">
      <a href="#">Home</a><a href="#">Our Services</a><a href="#">About us</a><a href="#">Our Products</a><a href="#">Contact us</a>
    </div>
    <div class="footer-brand"><span></span><span>Marlune</span></div>
    <div class="copy">Marlune solutions © 2012 | Privacy Policy</div>
    <div class="contact">
      <h2>CONTACT US</h2>
      <p style="top:55px">sales@marlune-example.ca</p>
      <p style="top:86px">PO Box ~~~~~~<br>Calgary, AB<br>T9Z 0Q1</p>
    </div>
  </footer>
</div>
</body>
</html>
```